Korvex Systems*

Stationary design including business cards, letter heads, envelops and email signatures using our new logo

Target Market(s)

Innovative Technologies

Industry/Entity Type

Defense Contracting

Font styles to use
Sans Serif

```html
<!DOCTYPE html>
<html lang="en">
<head>
<meta charset="utf-8">
<title>Korvex Systems Stationery</title>
<link href="https://fonts.googleapis.com/css2?family=Oswald:wght@400;500&family=Lato:wght@400;700&family=Open+Sans:wght@400&family=Pinyon+Script&display=swap" rel="stylesheet">
<style>
:root{
  --backdrop:#dcd9d5;
  --paper:#ffffff;
  --ink:#1c1c1c;
  --text:#575757;
  --muted:#6b6b6b;
  --dark:#2b2a2a;
  --dark-name:#4a4a4a;
}
*{margin:0;padding:0;box-sizing:border-box}
html,body{width:1200px;height:842px;overflow:hidden;background:var(--backdrop)}
.canvas{position:relative;width:1200px;height:842px}
.sheet{position:absolute;background:var(--paper);box-shadow:0 2px 8px rgba(0,0,0,.18);overflow:hidden}
.brand-name{font-family:'Oswald',sans-serif;font-weight:400;color:var(--ink);letter-spacing:-.2px;line-height:1;white-space:nowrap}
.contact{font-family:'Open Sans',sans-serif;color:var(--muted);line-height:1.12;font-style:normal}
.contact .gap{height:.8em}
.contact .row{display:flex;align-items:center;gap:.35em}
.contact svg{width:.8em;height:.8em;flex:none}

/* letterhead */
.letterhead{left:60px;top:70px;width:495px;height:701px}
.letterhead .brand-name{position:absolute;left:42px;top:78px;font-size:16px}
.letterhead .contact{position:absolute;left:345px;top:31px;font-size:8.4px}
.letter{position:absolute;left:52px;top:152px;width:390px;font-family:'Lato',sans-serif;font-weight:400;color:var(--text);font-size:8.1px;line-height:11.7px}
.letter .date{margin-bottom:12px}
.letter .recipient strong{font-weight:700;color:var(--ink)}
.letter .salutation{margin:18px 0 11px}
.letter p.body{text-align:justify;margin-bottom:11.7px}
.letter .closing{margin-top:36px}
.letter .signature{font-family:'Pinyon Script',cursive;font-weight:400;font-size:16px;color:var(--ink);margin-top:6px}

/* business cards */
.card{top:113px;width:231px;height:132px}
.card-front{left:571px}
.card-front .person{position:absolute;left:18px;top:23px}
.card-front .person-name{font-family:'Oswald',sans-serif;font-weight:500;font-size:9px;color:var(--ink);letter-spacing:-.1px}
.card-front .person-title{font-family:'Open Sans',sans-serif;font-size:5px;color:var(--muted)}
.card-front .contact{position:absolute;left:19px;top:62px;font-size:5px}
.card-front .brand-name{position:absolute;right:18px;top:90px;font-size:14px}
.card-back{left:816px;background:var(--dark)}
.card-back .brand-name{position:absolute;left:0;right:0;top:90px;text-align:center;font-size:14px;color:var(--dark-name)}

/* compliment slip */
.slip{left:571px;top:260px;width:570px;height:248px}
.slip .brand-name{position:absolute;left:39px;top:87px;font-size:16px}
.slip .contact{position:absolute;left:40px;top:154px;font-size:8.4px}

/* envelope */
.envelope{left:571px;top:524px;width:570px;height:247px}
.envelope .flap{position:absolute;left:0;top:0;width:570px;height:84px}
.envelope .brand-name{position:absolute;left:0;right:0;top:22px;text-align:center;font-size:26px;color:var(--paper)}
</style>
</head>
<body>
<svg width="0" height="0" style="position:absolute" aria-hidden="true">
  <defs>
    <symbol id="icon-phone" viewBox="0 0 10 10"><path d="M2.2 1l1.5 1.8-.9 1.1c.6 1.2 1.6 2.2 2.8 2.8l1.1-.9L8.5 7.3 7.6 9C4.3 8.6 1.4 5.7 1 2.4z" fill="currentColor"/></symbol>
    <symbol id="icon-mail" viewBox="0 0 10 10"><rect x="1" y="2.5" width="8" height="5.5" fill="currentColor"/><path d="M1 2.5l4 3 4-3" stroke="#fff" stroke-width=".8" fill="none"/></symbol>
    <symbol id="icon-web" viewBox="0 0 10 10"><g fill="none" stroke="currentColor" stroke-width=".9"><circle cx="5" cy="5" r="4"/><ellipse cx="5" cy="5" rx="1.7" ry="4"/><path d="M1 5h8"/></g></symbol>
  </defs>
</svg>

<main class="canvas">
  <section class="sheet letterhead">
    <div class="brand-name">KORVEX SYSTEMS</div>
    <address class="contact">
      <div>Korvex Systems</div>
      <div>418 Harbor Road</div>
      <div>Eastfield 210, XY, 4100</div>
      <div class="gap"></div>
      <div class="row"><svg><use href="#icon-phone"/></svg>+1.300.555.0142</div>
      <div class="row"><svg><use href="#icon-mail"/></svg>hello@korvexsystems.com</div>
      <div class="row"><svg><use href="#icon-web"/></svg>www.korvexsystems.com</div>
    </address>
    <article class="letter">
      <div class="date">01 January 2050</div>
      <div class="recipient">
        <strong>Larkfield Holdings Ltd.</strong><br>
        PO Box 7120 Linden Ave<br>
        Westbrook City Country 7120
      </div>
      <div class="salutation">Dear Martin Ellery,</div>
      <p class="body">Lorem ipsum dolor sit amet, consectetuer adipiscing elit, sed diam nonummy nibh euismod tincidunt ut laoreet dolore magna aliquam erat volutpat. Ut wisi enim ad minim veniam, quis nostrud exerci tation ullamcorper suscipit lobortis nisl ut aliquip ex ea commodo consequat. Duis dolore te feugait nulla facilisi. Nam liber tempor cum soluta nobis eleifend option congue nihil imperdiet doming id quod mazim placerat facer possim assum. Lorem ipsum dolor sit amet, consectetuer adipiscing elit, sed diam nonummy nibh euismod tincidunt ut laoreet dolore magna aliquam erat volutpat. Ut wisi enim ad minim veniam, quis nostrud exerci tation ullamcorper suscipit lobortis nisl ut aliquip ex ea commodo consequat.</p>
      <p class="body">Consectetuer adipiscing elit, sed diam nonummy nibh euismod tincidunt ut laoreet dolore magna aliquam erat volutpat. Ut wisi enim ad minim veniam, quis nostrud exerci tation ullamcorper suscipit lobortis nisl ut aliquip ex ea commodo consequat. Consectetuer adipiscing elit, sed diam nonummy nibh euismod tincidunt ut laoreet dolore magna aliquam erat volutpat. Ut wisi enim ad minim veniam, quis nostrud exerci tation ullamcorper suscipit lobortis nisl ut aliquip ex ea commodo consequat.</p>
      <p class="body">Consectetuer adipiscing elit, sed diam nonummy nibh euismod tincidunt ut laoreet dolore magna aliquam erat volutpat. Ut wisi enim ad minim veniam, quis nostrud exerci tation ullamcorper suscipit lobortis nisl ut aliquip ex ea commodo consequat. Consectetuer adipiscing elit, sed diam nonummy nibh euismod tincidunt ut laoreet dolore magna aliquam erat volutpat. Ut wisi enim ad minim veniam, quis nostrud exerci tation ullamcorper suscipit lobortis nisl ut aliquip ex ea commodo consequat.</p>
      <div class="closing">Sincerely Yours</div>
      <div class="signature">Thomas Reed Callen</div>
    </article>
  </section>

  <section class="sheet card card-front">
    <div class="person">
      <div class="person-name">DANIEL MARSH</div>
      <div class="person-title">Managing Director</div>
    </div>
    <address class="contact">
      <div>Korvex Systems</div>
      <div>418 Harbor Road</div>
      <div>Eastfield 210, XY, 4100</div>
      <div class="gap"></div>
      <div class="row"><svg><use href="#icon-phone"/></svg>+1.300.555.0142</div>
      <div class="row"><svg><use href="#icon-mail"/></svg>hello@korvexsystems.com</div>
      <div class="row"><svg><use href="#icon-web"/></svg>www.korvexsystems.com</div>
    </address>
    <div class="brand-name">KORVEX SYSTEMS</div>
  </section>

  <section class="sheet card card-back">
    <div class="brand-name">KORVEX SYSTEMS</div>
  </section>

  <section class="sheet slip">
    <div class="brand-name">KORVEX SYSTEMS</div>
    <address class="contact">
      <div>Korvex Systems</div>
      <div>418 Harbor Road</div>
      <div>Eastfield 210, XY, 4100</div>
      <div class="gap"></div>
      <div class="row"><svg><use href="#icon-phone"/></svg>+1.300.555.0142</div>
      <div class="row"><svg><use href="#icon-mail"/></svg>hello@korvexsystems.com</div>
      <div class="row"><svg><use href="#icon-web"/></svg>www.korvexsystems.com</div>
    </address>
  </section>

  <section class="sheet envelope">
    <svg class="flap" viewBox="0 0 570 84" aria-hidden="true">
      <path d="M0 0H570L543 66Q537 81 520 81H50Q33 81 27 66Z" fill="var(--dark)"/>
    </svg>
    <div class="brand-name">KORVEX SYSTEMS</div>
  </section>
</main>
</body>
</html>
```